Westbrook Valley Federal Credit Union need business Expo Booth Advertising

We need art work For A business Expo booth. We are a federal Credit Union that offers Savings accounts, Checking Accounts, Money Market Accounts, Special savings accounts such as Vacation, and Lantern Circle savings accounts. We offer New or used car loans, Motorcycle loans, Boat loans, Personal Loans, Mortgage loans. Quorva Loans. We offer Debit cards. We have free electronic banking, free bill pay. We are a not-for Profit financial Institution that is owned by it's account holders. We participate in a share branch network of credit unions. We only serve member of our Select Employee Groups. We will be celebrating 80 years in business next year on 03-26-2015. We would like the final Design to appeal to consumer eye, and communicate that we transition with the times to serve our members needs no matter where they go, and what they need, we are here for them. I uploaded a sample picture of the items that we want to print Art work on. I also uploaded our current logos, in a few different formats.

Target Market(s)

Audience for the design will be younger generation 18 to 40, both male and female.

Industry/Entity Type

Electronic

Requirements
Must have
• Must have logo and name of company
Nice to have
• Nice to have images that would represent the services we offer instead of text. I love layering of images, and images that make you think.
Should not have
• Do not include specific information on hours incase they should change. Do not include specific detail on current specials, but could say inquire or ask about our Great Loan Specials.

```html
<!DOCTYPE html>
<html lang="en">
<head>
<meta charset="utf-8">
<title>Westbrook Valley Federal Credit Union – Expo Banners</title>
<link rel="stylesheet" href="https://fonts.googleapis.com/css2?family=Ubuntu:ital,wght@0,400;0,500;0,700;1,500;1,700&display=swap">
<style>
  :root {
    --stage-top: #f2f2f2;
    --stage-bottom: #b9b9b9;
    --panel-top: #ffffff;
    --panel-mid: #e6e4f4;
    --panel-bottom: #aeaadb;
    --ink: #25252f;
    --ink-soft: #8b8a91;
    --heading-light: #c9c8d2;
    --heading-edge: #9e9da8;
    --band: #2f6867;
    --band-text: #ffffff;
    --tile-top: #fbfbfd;
    --tile-bottom: #d8d7e2;
    --icon-dark: #3a3a42;
    --icon-light: #e9e9ef;
  }
  * { box-sizing: border-box; margin: 0; padding: 0; }
  html, body { width: 1200px; height: 900px; overflow: hidden; }
  body {
    font-family: "Ubuntu", sans-serif;
    background: linear-gradient(180deg, var(--stage-top), var(--stage-bottom));
    position: relative;
  }
  .banner {
    position: absolute;
    top: 3px;
    width: 357px;
    height: 890px;
    background: linear-gradient(180deg, var(--panel-top) 8%, var(--panel-mid) 45%, var(--panel-bottom) 85%);
    border: 1px solid #777;
    box-shadow: 0 0 6px rgba(0,0,0,.35);
    overflow: hidden;
  }
  .banner--anniversary { left: 34px; }
  .banner--services { left: 421px; }
  .banner--about { left: 809px; }

  .brand {
    position: absolute;
    top: 40px; left: 26px;
    display: flex; align-items: center; gap: 14px;
  }
  .brand__dot { width: 62px; height: 62px; border-radius: 50%; background: var(--ink); flex: none; }
  .brand__name {
    font-weight: 500; font-size: 21px; line-height: 27px; color: var(--ink); white-space: nowrap;
  }

  .handshake {
    position: absolute; left: 0; top: 596px; width: 100%; height: 160px;
    background: linear-gradient(180deg, #b9b6d6 0%, #55536a 40%, #2e2d38 65%, #9d9ac4 100%);
    opacity: .85;
  }
  .tagline {
    position: absolute; top: 773px; width: 100%; text-align: center;
    font-style: italic; font-weight: 700; font-size: 25px; color: var(--ink);
  }
  .band {
    position: absolute; bottom: 0; left: 0; width: 100%; height: 71px;
    background: var(--band); color: var(--band-text);
    display: flex; align-items: center; justify-content: center;
    font-style: italic; font-weight: 700; font-size: 20px; white-space: nowrap;
  }

  /* Anniversary */
  .celebrate { position: absolute; left: 0; width: 100%; text-align: center; transform: rotate(-8deg); white-space: nowrap; }
  .celebrate__lead { top: 232px; font-size: 33px; font-weight: 700; color: var(--ink-soft); letter-spacing: -0.5px; }
  .celebrate__number {
    top: 250px; left: 4px; font-size: 210px; font-weight: 700; color: var(--ink);
    line-height: 1; transform: none; letter-spacing: -8px;
  }
  .celebrate__tail { top: 452px; left: 20px; font-size: 31px; line-height: 36px; font-weight: 700; color: var(--ink-soft); letter-spacing: -0.5px; }

  /* Services */
  .service { position: absolute; left: 28px; width: 320px; height: 94px; }
  .service--loans { top: 173px; }
  .service--accounts { top: 317px; }
  .service--cards { top: 470px; }
  .service__tile {
    position: absolute; left: 0; top: 0; width: 130px; height: 94px; border-radius: 8px;
    background: linear-gradient(180deg, var(--tile-top), var(--tile-bottom));
    box-shadow: 1px 2px 4px rgba(0,0,0,.35);
  }
  .service__tile::after {
    content: ""; position: absolute; inset: 14px 18px; border-radius: 4px;
    background: linear-gradient(135deg, #9a9aa3, #3c3c44);
  }
  .service__title {
    position: absolute; left: 136px; top: 0;
    font-style: italic; font-weight: 700; font-size: 28px; line-height: 34px; color: var(--heading-light);
    -webkit-text-stroke: .6px var(--heading-edge);
    white-space: nowrap; letter-spacing: -0.8px;
  }
  .service__icon {
    position: absolute; width: 40px; height: 40px; border-radius: 50%;
    background: radial-gradient(circle at 40% 35%, var(--icon-light), #bdbcc8 60%, #8d8c98);
    box-shadow: 1px 1px 3px rgba(0,0,0,.35);
  }
  .service__icon::after {
    content: ""; position: absolute; inset: 11px; border-radius: 50%; background: var(--icon-dark);
  }
  .service__caption {
    position: absolute; width: 70px; text-align: center; font-size: 8px; font-style: italic; color: var(--ink); white-space: nowrap;
  }
  .service__perks {
    position: absolute; left: 152px; top: 45px;
    font-style: italic; font-weight: 700; font-size: 13px; line-height: 19px; color: var(--ink); white-space: nowrap;
  }

  /* About */
  .about { position: absolute; left: 0; width: 100%; text-align: center; transform: rotate(-9deg); white-space: nowrap; }
  .about__heading { font-weight: 700; color: var(--ink); }
  .about__rule { height: 3px; margin: 2px auto 4px; width: 360px; background: linear-gradient(90deg, var(--ink), #8e8d96 70%, var(--ink)); }
  .about__text { font-weight: 700; color: var(--ink-soft); font-size: 29px; line-height: 34px; letter-spacing: -0.5px; }
  .about--who { top: 215px; }
  .about--who .about__heading { font-size: 47px; padding-left: 60px; letter-spacing: -0.5px; }
  .about--owner { top: 400px; }
  .about--owner .about__heading { font-size: 28px; letter-spacing: -0.5px; }
</style>
</head>
<body>

<section class="banner banner--anniversary">
  <header class="brand">
    <span class="brand__dot"></span>
    <span class="brand__name">Westbrook Valley<br>Federal Credit Union</span>
  </header>
  <p class="celebrate celebrate__lead">We are celebrating!</p>
  <p class="celebrate celebrate__number">80</p>
  <p class="celebrate celebrate__tail">years in business<br>serving your needs</p>
  <div class="handshake" role="img" aria-label="Engraved-style illustration of two hands in suit sleeves shaking"></div>
  <p class="tagline">We’ll be with You!</p>
  <footer class="band">Whewever you go...</footer>
</section>

<section class="banner banner--services">
  <header class="brand">
    <span class="brand__dot"></span>
    <span class="brand__name">Westbrook Valley<br>Federal Credit Union</span>
  </header>

  <div class="service service--loans">
    <div class="service__tile" role="img" aria-label="Stacks of banknotes"></div>
    <h2 class="service__title">LOANS</h2>
    <span class="service__icon" style="left:266px;top:4px" role="img" aria-label="House"></span>
    <span class="service__icon" style="left:160px;top:56px" role="img" aria-label="Car"></span>
    <span class="service__icon" style="left:213px;top:56px" role="img" aria-label="Boat"></span>
    <span class="service__icon" style="left:266px;top:56px" role="img" aria-label="Motorcycle"></span>
  </div>

  <div class="service service--accounts">
    <div class="service__tile" role="img" aria-label="Vault safe door"></div>
    <h2 class="service__title">ACCOUNTS</h2>
    <span class="service__icon" style="left:160px;top:55px" role="img" aria-label="Checking"></span>
    <span class="service__icon" style="left:213px;top:55px" role="img" aria-label="Money market"></span>
    <span class="service__icon" style="left:266px;top:55px" role="img" aria-label="Savings"></span>
    <span class="service__caption" style="left:145px;top:97px">Checking</span>
    <span class="service__caption" style="left:198px;top:97px">Money market</span>
    <span class="service__caption" style="left:251px;top:97px">Savings</span>
  </div>

  <div class="service service--cards">
    <div class="service__tile" role="img" aria-label="Debit card laid over banknotes"></div>
    <h2 class="service__title">DEBIT CARDS</h2>
    <p class="service__perks">FREE electronic banking<br>FREE bill pay</p>
  </div>

  <div class="handshake" role="img" aria-label="Engraved-style illustration of two hands in suit sleeves shaking"></div>
  <footer class="band">Ask about our Great Loan Specials!</footer>
</section>

<section class="banner banner--about">
  <header class="brand">
    <span class="brand__dot"></span>
    <span class="brand__name">Westbrook Valley<br>Federal Credit Union</span>
  </header>
  <div class="about about--who">
    <h2 class="about__heading">Who we are?</h2>
    <div class="about__rule"></div>
    <p class="about__text">We are a not-for-profit<br>financial Institute</p>
  </div>
  <div class="about about--owner">
    <h2 class="about__heading">Become an owner today!</h2>
    <div class="about__rule"></div>
    <p class="about__text">We are owned by our<br>account holders</p>
  </div>
  <div class="handshake" role="img" aria-label="Engraved-style illustration of two hands in suit sleeves shaking"></div>
  <p class="tagline">We’ll be with You!</p>
  <footer class="band">Whewever you go...</footer>
</section>

</body>
</html>
```